Visitenkarten-Design für Gesundheits- und Ernährungsberaterin
Tolle Kommunikation und Umsetzung meiner Vorstellungen. Viele Vorschläge und zügige Antworten auf jegliche Fragen. Immer wieder gerne. Großartige Zusammenarbeit und ein noch größeres Dankeschön
Zielgruppe
Ich bin Gesundheit und Ernährungsberaterin
Zielgruppe sind chronisch Kranke und Gesundheitsbewusste Personen
Aufgabenstellung
Schlichtes aber direkt erkennbares Design.
Koste den Morgen , Gesundheit und Ernährungsberatung ( gut lesbar , elegant)
Miriam Holtkamp-Berger ( nicht so groß )
Grau ; Grün Töne und gerne etwas rosa
Infos wie Adresse und E-Mail vielleicht in jeweilige Blöcke am unteren Rand

```html
<!DOCTYPE html>
<html lang="de">
<head>
<meta charset="utf-8">
<title>Visitenkarten – Miriam Holtkamp-Berger</title>
<link rel="stylesheet" href="https://fonts.googleapis.com/css2?family=Montserrat:ital,wght@0,400;0,500;0,700;1,300&display=swap">
<style>
  :root {
    --green: #8cd35f;
    --pink: #dc8885;
    --grey: #666666;
    --text: #555555;
    --paper: #ffffff;
    --page: #ffffff;
  }
  * { box-sizing: border-box; margin: 0; padding: 0; }
  html, body { width: 861px; height: 1200px; overflow: hidden; background: var(--page); }
  body { position: relative; font-family: "Montserrat", sans-serif; color: var(--text); }

  .card {
    position: absolute;
    width: 340px;
    height: 223px;
    background: var(--paper);
    box-shadow: 4px 4px 7px rgba(0, 0, 0, 0.28);
    overflow: hidden;
  }
  .card::before {
    content: "";
    position: absolute;
    left: 0; top: 0; bottom: 0;
    width: 10px;
    background: var(--edge);
  }
  .card--front { left: 68px; }
  .card--back  { left: 443px; }
  .row-1 { top: 55px; }
  .row-2 { top: 342px; }
  .row-3 { top: 629px; }
  .row-4 { top: 913px; }
  .edge-green { --edge: var(--green); }
  .edge-grey  { --edge: var(--grey); }
  .edge-pink  { --edge: var(--pink); }
  .card--filled { background: var(--green); }

  /* Wortmarke */
  .brand {
    position: absolute;
    display: flex;
    flex-direction: column;
    align-items: center;
    color: var(--green);
    font-weight: 500;
    white-space: nowrap;
  }
  .brand__dot { border-radius: 50%; background: currentColor; }
  .card--front .brand { left: 10px; right: 0; top: 42px; gap: 10px; font-size: 15px; letter-spacing: 0.5px; }
  .card--front .brand__dot { width: 50px; height: 50px; }
  .card--filled .brand { color: var(--paper); }
  .card--back .brand { right: 14px; width: 90px; top: 12px; gap: 6px; font-size: 8px; }
  .card--back .brand__dot { width: 32px; height: 32px; }

  .tagline {
    position: absolute;
    font-style: italic;
    font-weight: 300;
    text-transform: uppercase;
    letter-spacing: 1.2px;
    color: var(--pink);
    white-space: nowrap;
  }
  .card--front .tagline { left: 10px; right: 0; top: 161px; text-align: center; font-size: 13.5px; }
  .card--filled .tagline { color: var(--paper); }
  .card--back .tagline { right: 9px; top: 96px; font-size: 9.5px; letter-spacing: 0.9px; }

  .person { position: absolute; left: 18px; top: 140px; text-transform: uppercase; }
  .person__name { font-weight: 700; font-size: 10.5px; line-height: 12px; letter-spacing: 0.2px; }
  .person__role { font-size: 6.3px; line-height: 8px; letter-spacing: 0.1px; }

  .address, .contact {
    position: absolute;
    font-size: 8px;
    line-height: 10.6px;
    text-transform: uppercase;
    white-space: nowrap;
  }
  .address { left: 18px; top: 198px; }
  .contact {
    left: 166px;
    right: 9px;
    top: 187px;
    display: grid;
    grid-template-columns: 34px auto;
  }
</style>
</head>
<body>

  <!-- Reihe 1 -->
  <section class="card card--front edge-green row-1">
    <div class="brand"><span class="brand__dot"></span>Holtkamp-Berger</div>
    <p class="tagline">Koste den Morgen.</p>
  </section>
  <section class="card card--back edge-green row-1">
    <div class="brand"><span class="brand__dot"></span>Holtkamp-Berger</div>
    <p class="tagline">Koste den Morgen.</p>
    <div class="person"><p class="person__name">Miriam Holtkamp-Berger</p><p class="person__role">Gesundheits- und Ernährungsberaterin</p></div>
    <p class="address">Wiesenstieg 7<br>27412 Brunsholt</p>
    <dl class="contact"><dt>Tel</dt><dd>04521 / 770 24 16</dd><dt>Mobil</dt><dd>0152 / 38 07 61 25</dd><dt>Mail</dt><dd>info-mhb@kornpost.de</dd></dl>
  </section>

  <!-- Reihe 2 -->
  <section class="card card--front edge-grey row-2">
    <div class="brand"><span class="brand__dot"></span>Holtkamp-Berger</div>
    <p class="tagline">Koste den Morgen.</p>
  </section>
  <section class="card card--back edge-grey row-2">
    <div class="brand"><span class="brand__dot"></span>Holtkamp-Berger</div>
    <p class="tagline">Koste den Morgen.</p>
    <div class="person"><p class="person__name">Miriam Holtkamp-Berger</p><p class="person__role">Gesundheits- und Ernährungsberaterin</p></div>
    <p class="address">Wiesenstieg 7<br>27412 Brunsholt</p>
    <dl class="contact"><dt>Tel</dt><dd>04521 / 770 24 16</dd><dt>Mobil</dt><dd>0152 / 38 07 61 25</dd><dt>Mail</dt><dd>info-mhb@kornpost.de</dd></dl>
  </section>

  <!-- Reihe 3 -->
  <section class="card card--front edge-pink row-3">
    <div class="brand"><span class="brand__dot"></span>Holtkamp-Berger</div>
    <p class="tagline">Koste den Morgen.</p>
  </section>
  <section class="card card--back edge-pink row-3">
    <div class="brand"><span class="brand__dot"></span>Holtkamp-Berger</div>
    <p class="tagline">Koste den Morgen.</p>
    <div class="person"><p class="person__name">Miriam Holtkamp-Berger</p><p class="person__role">Gesundheits- und Ernährungsberaterin</p></div>
    <p class="address">Wiesenstieg 7<br>27412 Brunsholt</p>
    <dl class="contact"><dt>Tel</dt><dd>04521 / 770 24 16</dd><dt>Mobil</dt><dd>0152 / 38 07 61 25</dd><dt>Mail</dt><dd>info-mhb@kornpost.de</dd></dl>
  </section>

  <!-- Reihe 4 -->
  <section class="card card--front card--filled edge-pink row-4">
    <div class="brand"><span class="brand__dot"></span>Holtkamp-Berger</div>
    <p class="tagline">Koste den Morgen.</p>
  </section>
  <section class="card card--back edge-pink row-4">
    <div class="brand"><span class="brand__dot"></span>Holtkamp-Berger</div>
    <p class="tagline">Koste den Morgen.</p>
    <div class="person"><p class="person__name">Miriam Holtkamp-Berger</p><p class="person__role">Gesundheits- und Ernährungsberaterin</p></div>
    <p class="address">Wiesenstieg 7<br>27412 Brunsholt</p>
    <dl class="contact"><dt>Tel</dt><dd>04521 / 770 24 16</dd><dt>Mobil</dt><dd>0152 / 38 07 61 25</dd><dt>Mail</dt><dd>info-mhb@kornpost.de</dd></dl>
  </section>

</body>
</html>
```